Coffee House With Cycling Theme Wants Business Cards

We want to create a business card for a coffee house that has a cycling theme. We expect to use the current logo on one side of the business card and we have been considering adding the words 'COFFEE HOUSE' underneath (see example). For the other side of the business card we want an interesting design with tag-line, address and social media links (the normal business card stuff). See examples provided but we are not fixed on having it exactly as shown, we are very open to great creative ideas. Please note our logo has the initials ‘RM' in orange embedded in the design and this must be retained. However, you can play with the words COFFEE HOUSE as well as use the orange color on the backside of the business card, as you see fit. For an image on the backside of the business card it can be a photo, hand-drawn or whatever but it must visually combine coffee and cycling in some way. The interior of the Coffee House will be reclaimed wood, rustic and have an urban feel to it with cycling artifacts hanging from the walls/ceiling, etc. Finally, it would be beneficial if the business card design elements can be easily used on flyers and other promotional assets. Good luck, we are looking forward to seeing your creative ideas.

Target Market(s)

Coffee lovers and cycling fans

Contact Information for Business Card

See project description.

Colors

Designer to choose colors to be used in the design.

Requirements
Must have
• Must use the current logo provided and combine a coffee and bike theme.
Nice to have
• Orange is used in current logo and could be used as an accent color on the backside of the business card.

```html
<!DOCTYPE html>
<html lang="en">
<head>
<meta charset="utf-8">
<title>RM Coffee House – Business Cards</title>
<link rel="stylesheet" href="https://fonts.googleapis.com/css2?family=Montserrat:wght@400&display=swap">
<style>
  :root {
    --backdrop: #c9c9cb;
    --card-white: #ffffff;
    --band-white: #f3f3f3;
    --brand-orange: #f26a2a;
    --ink: #3a3a3a;
    --ink-dark: #1c1c1c;
  }
  * { box-sizing: border-box; margin: 0; padding: 0; }
  html, body {
    width: 1200px; height: 799px; overflow: hidden;
    background: var(--backdrop);
    font-family: "Montserrat", sans-serif;
  }
  .card {
    position: absolute; left: 290px;
    width: 620px; height: 354px;
    background: var(--card-white);
    box-shadow: 0 4px 14px rgba(0,0,0,0.18);
    overflow: hidden;
  }
  .card--front { top: 30px; background: var(--band-white); }
  .card--back { top: 415px; }

  .band { position: absolute; left: 0; right: 0; height: 80px; background: var(--brand-orange); }
  .band--top { top: 0; }
  .band--bottom { bottom: 0; }

  .wordmark {
    position: absolute;
    display: flex; align-items: center; justify-content: center; gap: 12px;
    color: var(--ink); font-weight: 400; line-height: 1;
    white-space: nowrap;
  }
  .wordmark__dot {
    width: 18px; height: 18px; border-radius: 50%;
    background: var(--brand-orange); flex: none;
  }
  .card--front .wordmark { left: 0; right: 0; top: 160px; font-size: 30px; }
  .card--back .wordmark { left: 20px; width: 300px; top: 166px; font-size: 24px; }

  .contact-rail {
    position: absolute; left: 349px; top: 48px;
    width: 2px; height: 262px; background: var(--ink-dark);
  }
  .contact-rail::before, .contact-rail::after {
    content: ""; position: absolute; left: -4px;
    width: 10px; height: 10px; border-radius: 50%; background: var(--ink-dark);
  }
  .contact-rail::before { top: -4px; }
  .contact-rail::after { bottom: -4px; }

  .contact-list { position: absolute; left: 332px; top: 64px; list-style: none; }
  .contact-item {
    display: flex; align-items: center; height: 36px; margin-bottom: 10px;
    font-size: 17px; color: var(--ink-dark);
  }
  .contact-icon { width: 36px; height: 36px; margin-right: 14px; flex: none; }
</style>
</head>
<body>

<section class="card card--front" aria-label="Business card front">
  <div class="band band--top"></div>
  <div class="wordmark">
    <span class="wordmark__dot"></span>
    <span class="wordmark__name">RM Coffee House</span>
  </div>
  <div class="band band--bottom"></div>
</section>

<section class="card card--back" aria-label="Business card back">
  <div class="wordmark">
    <span class="wordmark__dot"></span>
    <span class="wordmark__name">RM Coffee House</span>
  </div>

  <div class="contact-rail"></div>
  <ul class="contact-list">
    <li class="contact-item">
      <svg class="contact-icon" viewBox="0 0 36 36"><circle cx="18" cy="18" r="16" fill="#fff" stroke="#1c1c1c" stroke-width="2"/><circle cx="18" cy="18" r="11" fill="#1c1c1c"/></svg>
      rmcoffeehouse
    </li>
    <li class="contact-item">
      <svg class="contact-icon" viewBox="0 0 36 36"><circle cx="18" cy="18" r="16" fill="#fff" stroke="#1c1c1c" stroke-width="2"/><circle cx="18" cy="18" r="11" fill="#1c1c1c"/></svg>
      rmcoffeehouse
    </li>
    <li class="contact-item">
      <svg class="contact-icon" viewBox="0 0 36 36"><circle cx="18" cy="18" r="16" fill="#fff" stroke="#1c1c1c" stroke-width="2"/><circle cx="18" cy="18" r="11" fill="#1c1c1c"/><rect x="12" y="14" width="12" height="8" fill="#fff"/><path d="M12 14 L18 19 L24 14" fill="none" stroke="#1c1c1c" stroke-width="1.2"/></svg>
      info@rmcoffeehouse.com
    </li>
    <li class="contact-item">
      <svg class="contact-icon" viewBox="0 0 36 36"><circle cx="18" cy="18" r="16" fill="#fff" stroke="#1c1c1c" stroke-width="2"/><circle cx="18" cy="18" r="11" fill="#1c1c1c"/><g fill="none" stroke="#fff" stroke-width="1.2"><circle cx="18" cy="18" r="6.5"/><ellipse cx="18" cy="18" rx="3" ry="6.5"/><line x1="11.5" y1="18" x2="24.5" y2="18"/></g></svg>
      www.rmcoffeehouse.com
    </li>
    <li class="contact-item">
      <svg class="contact-icon" viewBox="0 0 36 36"><circle cx="18" cy="18" r="16" fill="#fff" stroke="#1c1c1c" stroke-width="2"/><circle cx="18" cy="18" r="11" fill="#1c1c1c"/><path d="M18 25 C14 20 13.5 18 13.5 16 A4.5 4.5 0 0 1 22.5 16 C22.5 18 22 20 18 25 Z" fill="#fff"/><circle cx="18" cy="16" r="1.7" fill="#1c1c1c"/></svg>
      Maple Row, Eastbrook
    </li>
  </ul>
</section>

</body>
</html>
```